Vel-Trax.ch is looking for business card letterhead and envelope C5 with WOW effect

We need a strong business card for our company Vel-Trax.ch, logo is available. You want a black or dark background on which the logo Stark r% 26 # 252; appears. Letterhead and envelope in C5 format should be in a similar design, but does not have to be We need a strong business card for our company Vel-Trax.ch, logo is available. A black or dark background is desired, on which the logo Stark comes across. The letterhead and the envelope in C5 format should have a similar design.

Target Market(s)

Private customers as well as entrepreneurs

Contact Information for Business Card

E-mail: info@vel-trax.ch
Web.www.Vel-Trax.ch
Tel: +41 ( 0 ) 79 684 3027
Adresse:
Lindenhaldeweg 14
8617 Brenzikon

Hier kann man Icons verwenden für Email,Tel und Adressse

Font styles to use
Other font styles liked:
• Dubai,bold

Colors

Designer to choose colors to be used in the design.

Requirements
Must have
• WOW effect
Nice to have
• R% 26 # 252; back business card with our service listings. - VEHICLE LABELING - SHOP WINDOW LABELING - STICKERS AND MUCH MORE ... in red color

```html
<!DOCTYPE html>
<html lang="en">
<head>
<meta charset="utf-8">
<title>Vel-Trax.ch business card</title>
<link rel="stylesheet" href="https://fonts.googleapis.com/css2?family=Arimo:wght@400;700&display=swap">
<style>
  :root {
    --backdrop: #2a2a2a;
    --card: #1e1e1f;
    --card-back: #1b1b1c;
    --pattern-light: #2c2c2e;
    --white: #ffffff;
    --yellow: #f6c51a;
    --red: #e0161b;
    --rule: #6a6a6a;
  }
  * { margin: 0; padding: 0; box-sizing: border-box; }
  html, body { width: 1200px; height: 1108px; overflow: hidden; }
  body {
    background: var(--backdrop);
    font-family: "Arimo", Arial, sans-serif;
    position: relative;
  }
  .card {
    position: absolute;
    top: 234px;
    width: 400px;
    height: 640px;
    border-radius: 24px;
    overflow: hidden;
    color: var(--white);
  }
  .card-front { left: 160px; background: var(--card); }
  .card-back { left: 640px; background: var(--card-back); }

  .brand {
    position: absolute;
    left: 0; right: 0;
    display: flex;
    align-items: center;
    justify-content: center;
    gap: 16px;
  }
  .card-front .brand { top: 170px; }
  .card-back .brand { top: 360px; }
  .brand-mark {
    width: 34px; height: 34px;
    border-radius: 50%;
    background: var(--yellow);
  }
  .brand-name {
    font-weight: 700;
    font-size: 38px;
    color: var(--white);
    letter-spacing: 1px;
  }

  .contact-head {
    position: absolute;
    top: 372px; left: 40px; right: 40px;
    display: flex;
    align-items: center;
    gap: 10px;
  }
  .contact-head .rule { flex: 1; height: 1px; background: var(--rule); }
  .icon {
    width: 34px; height: 34px;
    border-radius: 5px;
    background: var(--yellow);
    display: flex; align-items: center; justify-content: center;
  }
  .icon svg { width: 22px; height: 22px; }

  .contact {
    position: absolute;
    top: 420px; left: 0; right: 0;
    text-align: center;
    font-size: 25px;
    line-height: 34px;
  }
  .contact .web { color: var(--yellow); }
  .divider {
    position: absolute;
    top: 530px; left: 70px; right: 70px;
    height: 1px; background: var(--rule);
  }
  .address {
    position: absolute;
    top: 548px; left: 0; right: 0;
    text-align: center;
    font-size: 25px;
    line-height: 34px;
  }

  .pattern {
    position: absolute;
    top: 0; left: 0; right: 0; height: 500px;
    background: radial-gradient(ellipse at 60% 30%, var(--pattern-light) 0%, var(--card-back) 75%);
  }
  .services {
    position: absolute;
    top: 520px; left: 0; right: 0;
    text-align: center;
    color: var(--red);
    font-size: 21px;
    line-height: 30px;
    text-transform: uppercase;
  }
</style>
</head>
<body>
  <section class="card card-front">
    <div class="brand">
      <span class="brand-mark"></span>
      <span class="brand-name">VEL-TRAX.CH</span>
    </div>

    <div class="contact-head">
      <span class="rule"></span>
      <span class="icon" aria-label="Phone">
        <svg viewBox="0 0 24 24"><path fill="#1e1e1f" d="M6.6 10.8a15 15 0 0 0 6.6 6.6l2.2-2.2c.3-.3.7-.4 1-.2 1.1.4 2.3.6 3.6.6.6 0 1 .4 1 1V20c0 .6-.4 1-1 1A17 17 0 0 1 3 4c0-.6.4-1 1-1h3.5c.6 0 1 .4 1 1 0 1.3.2 2.5.6 3.6.1.3 0 .7-.2 1z"/></svg>
      </span>
      <span class="icon" aria-label="Email">
        <svg viewBox="0 0 24 24"><rect x="3" y="6" width="18" height="12" fill="none" stroke="#1e1e1f" stroke-width="2"/><path d="M3 6l9 7 9-7" fill="none" stroke="#1e1e1f" stroke-width="2"/></svg>
      </span>
      <span class="icon" aria-label="Website">
        <svg viewBox="0 0 24 24"><circle cx="12" cy="12" r="9" fill="none" stroke="#1e1e1f" stroke-width="2"/><path d="M3 12h18M12 3c3 3 3 15 0 18M12 3c-3 3-3 15 0 18" fill="none" stroke="#1e1e1f" stroke-width="1.6"/></svg>
      </span>
      <span class="rule"></span>
    </div>

    <div class="contact">
      <p class="phone">+41 ( 0 ) 79 684 3027</p>
      <p class="email">info@vel-trax.ch</p>
      <p class="web">www.Vel-Trax.ch</p>
    </div>
    <div class="divider"></div>
    <div class="address">
      <p>Lindenhaldeweg 14</p>
      <p>8617 Brenzikon</p>
    </div>
  </section>

  <section class="card card-back">
    <div class="pattern" role="img" aria-label="Faint dark hexagon pattern"></div>
    <div class="brand">
      <span class="brand-mark"></span>
      <span class="brand-name">VEL-TRAX.CH</span>
    </div>
    <div class="services">
      <p>Vehicle labeling</p>
      <p>Shop window labeling</p>
      <p>Stickers and much more ...</p>
    </div>
  </section>
</body>
</html>
```